Letterhead for Law Firm - Logo already prepared

I previously used to prepare a logo which I was quite pleased with, a copy is attached for your reference. I would like the font of the logo to be all the same size, rather than the 'S' and 'L' being larger than the other letters.
I have copies of the attached in other formats if necessary.
I need a letterhead prepared which is virtually identical to the draft attached, however I will be adding an address, phone number, fax number, mobile number and email. I will provide these details with whoever can assist me.
I will also be providing insurance details to be listed at the foot of the page.
Finally, I need the file to be supplied as a high resolution pdf with 2mm bleed.
If you require any further information, please do not hesitate to contact me.

```html
<!DOCTYPE html>
<html lang="en">
<head>
<meta charset="utf-8">
<title>Veldhorst Legal – Letterhead</title>
<link rel="stylesheet" href="https://fonts.googleapis.com/css2?family=Marcellus+SC&family=Open+Sans:wght@400;600&display=swap">
<style>
  :root{
    --paper:#ffffff;
    --paper-shade:#f1f1f1;
    --ink:#1d1d1d;
    --orange:#f58a1f;
    --orange-deep:#e4531a;
    --grey:#7d7d7d;
    --grey-dark:#4a4a4a;
    --white:#ffffff;
  }
  *{box-sizing:border-box;margin:0;padding:0}
  html,body{width:948px;height:1200px;overflow:hidden;background:#e6e6e6}
  .letterhead{
    position:relative;width:948px;height:1200px;overflow:hidden;
    background:radial-gradient(ellipse at 50% 20%,var(--paper) 0%,var(--paper) 45%,var(--paper-shade) 100%);
    font-family:"Open Sans",Arial,sans-serif;
  }
  .brand{
    position:absolute;top:78px;left:0;width:100%;
    display:flex;justify-content:center;align-items:center;gap:18px;
  }
  .brand-dot{width:64px;height:64px;border-radius:50%;background:var(--orange)}
  .brand-name{
    font-family:"Marcellus SC",Georgia,serif;font-size:40px;letter-spacing:1px;
    color:var(--ink);text-transform:uppercase;
  }
  .footer-wave{position:absolute;left:0;top:1010px;width:948px;height:190px}
  .contact-list{
    position:absolute;right:66px;top:1046px;list-style:none;
    color:var(--white);font-size:14px;line-height:19px;text-align:right;
  }
  .contact-list li{display:flex;justify-content:flex-end;align-items:center;gap:8px}
  .contact-list .web{font-weight:600}
  .contact-icon{width:14px;height:14px;flex:none}
  .address{
    position:absolute;right:66px;top:1150px;color:var(--white);font-size:14px;
  }
  .insurance{
    position:absolute;left:62px;top:1146px;color:var(--white);font-size:24px;
  }
</style>
</head>
<body>
<main class="letterhead">
  <header class="brand">
    <span class="brand-dot"></span>
    <span class="brand-name">Veldhorst Legal</span>
  </header>

  <svg class="footer-wave" viewBox="0 0 948 190" aria-hidden="true">
    <defs>
      <linearGradient id="footerOrange" x1="0" y1="0" x2="1" y2="0.4">
        <stop offset="0" stop-color="var(--orange-deep)"/>
        <stop offset="0.6" stop-color="var(--orange)"/>
        <stop offset="1" stop-color="var(--orange-deep)"/>
      </linearGradient>
    </defs>
    <path d="M0,22 C160,78 360,105 540,58 S820,-4 948,8" fill="none" stroke="var(--grey)" stroke-width="9"/>
    <path d="M0,34 C160,88 360,112 540,68 S820,8 948,20" fill="none" stroke="var(--grey-dark)" stroke-width="4"/>
    <path d="M0,48 C160,100 350,122 540,82 S820,22 948,36 L948,190 L0,190 Z" fill="url(#footerOrange)"/>
    <path d="M0,48 C160,100 350,122 540,82 S820,22 948,36" fill="none" stroke="#ffb566" stroke-width="2"/>
  </svg>

  <ul class="contact-list">
    <li>55-0142-7300
      <svg class="contact-icon" viewBox="0 0 14 14"><circle cx="7" cy="7" r="6" fill="none" stroke="#fff" stroke-width="1.5"/><path d="M4.5 4h2l.5 2-1 .8a5 5 0 0 0 1.7 1.7l.8-1 2 .5v2c-4 .5-6.5-2-6-6z" fill="#fff"/></svg></li>
    <li>55-0142-7301
      <svg class="contact-icon" viewBox="0 0 14 14"><rect x="3" y="1" width="6" height="5" fill="#fff"/><rect x="2" y="6" width="10" height="7" rx="1" fill="#fff"/></svg></li>
    <li>55-0142-7302
      <svg class="contact-icon" viewBox="0 0 14 14"><rect x="4" y="1" width="6" height="12" rx="1.2" fill="#fff"/></svg></li>
    <li>name@veldhorstlegal.com
      <svg class="contact-icon" viewBox="0 0 14 14"><rect x="1" y="3" width="12" height="8" fill="#fff"/><path d="M1 3l6 5 6-5" fill="none" stroke="var(--orange)" stroke-width="1"/></svg></li>
    <li class="web">www.veldhorstlegal.com
      <svg class="contact-icon" viewBox="0 0 14 14"><circle cx="7" cy="7" r="6" fill="none" stroke="#fff" stroke-width="1.5"/><path d="M1 7h12M7 1c-3 3-3 9 0 12M7 1c3 3 3 9 0 12" fill="none" stroke="#fff" stroke-width="1"/></svg></li>
  </ul>

  <p class="insurance">insurance details..........</p>
  <p class="address">Suite000, Veldhorst bldg, Cityname, Countryname</p>
</main>
</body>
</html>
```